Business Card for KV

We need a double sided business card:

First Name Last Name
Cell 987-605-3214
mailbox@pelvaro-post.com

License #8096-WXYZ-2318
WFLMA # 60782
Hollin County

```html
<!DOCTYPE html>
<html lang="en">
<head>
<meta charset="utf-8">
<title>Kindred Valley — Business Card</title>
<link rel="stylesheet" href="https://fonts.googleapis.com/css2?family=Work+Sans:wght@400;500;700&display=swap">
<style>
  :root {
    --page: #e6e7e9;
    --navy: #2c4a68;
    --navy-soft: #36577a;
    --olive: #9b9838;
    --ink: #4d4f52;
    --paper: #ffffff;
  }
  * { box-sizing: border-box; margin: 0; padding: 0; }
  html, body { width: 1200px; height: 852px; overflow: hidden; }
  body {
    background: var(--page);
    font-family: "Work Sans", sans-serif;
    position: relative;
  }
  .card {
    position: absolute;
    top: 106px;
    width: 380px;
    height: 640px;
    border-radius: 22px;
    overflow: hidden;
    box-shadow: 0 10px 28px rgba(0,0,0,0.18);
  }
  .card--back { left: 190px; background: var(--navy); }
  .card--front { left: 630px; background: var(--paper); }

  .back-pattern {
    position: absolute; inset: 0;
    background: radial-gradient(circle at 50% 50%, var(--navy-soft), var(--navy) 70%);
  }
  .brand {
    position: absolute;
    left: 0; right: 0;
    display: flex; align-items: center; justify-content: center; gap: 12px;
    font-weight: 700;
    font-size: 30px;
    letter-spacing: 2px;
    text-transform: uppercase;
    white-space: nowrap;
  }
  .brand__dot { width: 20px; height: 20px; border-radius: 50%; flex: none; }
  .card--back .brand { top: 298px; color: var(--paper); }
  .card--back .brand__dot { background: var(--paper); }
  .card--front .brand { top: 72px; color: var(--navy); }
  .card--front .brand__dot { background: var(--olive); }

  .contact {
    position: absolute;
    left: 0; right: 0; top: 228px;
    text-align: center;
    color: var(--ink);
  }
  .contact__name {
    color: var(--olive);
    font-weight: 700;
    font-size: 27px;
    letter-spacing: 1px;
    text-transform: uppercase;
  }
  .contact__role { font-size: 17px; margin-top: 4px; }
  .contact__rule {
    width: 70px; height: 2px; background: var(--olive);
    margin: 16px auto 16px;
  }
  .contact__line { font-size: 17px; line-height: 1.55; }
  .contact__icons {
    display: flex; justify-content: center; gap: 8px;
    margin: 14px 0 10px;
  }
  .contact__icons svg { width: 14px; height: 14px; }
</style>
</head>
<body>
  <section class="card card--back">
    <div class="back-pattern" role="img" aria-label="Faint repeating leaf emblem pattern on navy"></div>
    <div class="brand"><span class="brand__dot"></span>Kindred Valley</div>
  </section>

  <section class="card card--front">
    <div class="brand"><span class="brand__dot"></span>Kindred Valley</div>
    <div class="contact">
      <p class="contact__name">Dorian Pell</p>
      <p class="contact__role">Founder</p>
      <div class="contact__rule"></div>
      <p class="contact__line">License #8096-WXYZ-2318</p>
      <p class="contact__line">WFLMA # 60782</p>
      <div class="contact__icons">
        <svg viewBox="0 0 16 16" aria-hidden="true"><path d="M4 1.5l2.2 3-1.4 1.6a9 9 0 0 0 5 5l1.6-1.4 3 2.2-1.2 2.3C7.5 14.5 1.5 8.5 1.7 2.7z" fill="var(--olive)"/></svg>
        <svg viewBox="0 0 16 16" aria-hidden="true"><rect x="1.5" y="3.5" width="13" height="9" fill="none" stroke="var(--olive)" stroke-width="1.6"/><path d="M1.5 3.5l6.5 5 6.5-5" fill="none" stroke="var(--olive)" stroke-width="1.6"/></svg>
        <svg viewBox="0 0 16 16" aria-hidden="true"><path d="M8 1a5 5 0 0 0-5 5c0 4 5 9 5 9s5-5 5-9a5 5 0 0 0-5-5z" fill="var(--olive)"/><circle cx="8" cy="6" r="1.8" fill="var(--paper)"/></svg>
      </div>
      <p class="contact__line">987-605-3214</p>
      <p class="contact__line">mailbox@pelvaro-post.com</p>
      <p class="contact__line">Hollin County</p>
    </div>
  </section>
</body>
</html>
```